New bussiness card, using company logo.
Lachlan Voss
Manager/Director
Birch Property Developments
Po Box 4657
Wrenfield Central
Tas
0455 386 218
lachlan@birchpropertydevelopments
eye catching, vibrant colours, professional

```html
<!DOCTYPE html>
<html lang="en">
<head>
<meta charset="utf-8">
<title>Birch Property Developments — Business Card</title>
<link rel="stylesheet" href="https://fonts.googleapis.com/css2?family=Quicksand:wght@400;500;700&display=swap">
<style>
  :root {
    --brand-red: #e4323f;
    --brand-green: #6cc24a;
    --card-white: #ffffff;
    --page-bg: #e6e6e6;
    --card-shadow: rgba(0, 0, 0, 0.18);
  }
  * { box-sizing: border-box; margin: 0; padding: 0; }
  html, body {
    width: 1200px;
    height: 900px;
    overflow: hidden;
    background: var(--page-bg);
    font-family: "Quicksand", sans-serif;
  }
  .canvas {
    width: 1200px;
    height: 900px;
    display: flex;
    flex-direction: column;
    align-items: center;
    justify-content: center;
    gap: 34px;
  }
  .card {
    position: relative;
    width: 700px;
    height: 400px;
    background: var(--card-white);
    box-shadow: 0 10px 28px var(--card-shadow);
    overflow: hidden;
  }

  /* Front face */
  .card-front {
    display: flex;
    align-items: center;
    justify-content: center;
  }
  .front-wordmark {
    display: flex;
    align-items: center;
    gap: 22px;
  }
  .wordmark-square {
    width: 46px;
    height: 46px;
    background: var(--brand-red);
    flex: none;
  }
  .wordmark-name {
    font-weight: 700;
    font-size: 40px;
    line-height: 1.05;
    letter-spacing: 0.02em;
    color: var(--brand-red);
    text-transform: uppercase;
  }

  /* Back face */
  .card-back { color: var(--brand-red); }
  .holder {
    position: absolute;
    left: 40px;
    top: 34px;
  }
  .holder-name {
    display: inline-block;
    font-weight: 700;
    font-size: 24px;
    padding-bottom: 4px;
    border-bottom: 3px solid var(--brand-red);
  }
  .holder-role,
  .holder-company {
    font-weight: 400;
    font-size: 19px;
    margin-top: 10px;
  }
  .address {
    position: absolute;
    right: 40px;
    top: 118px;
    text-align: right;
  }
  .address-wordmark {
    font-weight: 700;
    font-size: 13px;
    letter-spacing: 0.03em;
    text-transform: uppercase;
    color: var(--brand-red);
    margin-bottom: 14px;
  }
  .address-line {
    font-weight: 400;
    font-size: 19px;
    line-height: 1.9;
  }
  .accent-rule {
    position: absolute;
    left: 0;
    right: 0;
    bottom: 62px;
    height: 4px;
    background: var(--brand-green);
  }
  .contact-band {
    position: absolute;
    left: 0;
    right: 0;
    bottom: 0;
    height: 54px;
    background: var(--brand-red);
    color: var(--card-white);
    display: flex;
    align-items: center;
    justify-content: space-between;
    padding: 0 40px;
    font-size: 17px;
    font-weight: 500;
  }
  .contact-phone {
    display: flex;
    align-items: center;
    gap: 8px;
  }
  .phone-icon { width: 16px; height: 16px; }
</style>
</head>
<body>
<main class="canvas">

  <section class="card card-front" aria-label="Business card front">
    <div class="front-wordmark">
      <span class="wordmark-square"></span>
      <span class="wordmark-name">Birch<br>Property Developments</span>
    </div>
  </section>

  <section class="card card-back" aria-label="Business card back">
    <div class="holder">
      <h1 class="holder-name">Lachlan Voss</h1>
      <p class="holder-role">Manager/Director</p>
      <p class="holder-company">Birch Property Developments</p>
    </div>

    <div class="address">
      <p class="address-wordmark">Birch Property Developments</p>
      <p class="address-line">P.O. Box 4657</p>
      <p class="address-line">Wrenfield Central</p>
      <p class="address-line">Tas</p>
    </div>

    <div class="accent-rule"></div>

    <div class="contact-band">
      <span class="contact-phone">
        <svg class="phone-icon" viewBox="0 0 24 24" aria-hidden="true">
          <path fill="#ffffff" d="M6.6 10.8c1.4 2.8 3.8 5.1 6.6 6.6l2.2-2.2c.3-.3.7-.4 1-.2 1.1.4 2.3.6 3.6.6.6 0 1 .4 1 1V20c0 .6-.4 1-1 1C10.6 21 3 13.4 3 4c0-.6.4-1 1-1h3.5c.6 0 1 .4 1 1 0 1.3.2 2.5.6 3.6.1.3 0 .7-.2 1L6.6 10.8z"/>
        </svg>
        0455 386 218
      </span>
      <span class="contact-email">lachlan@birchpropertydevelopments.com</span>
    </div>
  </section>

</main>
</body>
</html>
```